Maplerise Trading Inc. needs an innovative idea for letterhead and visiting cards.

Maplerise Trading Inc. is a Canadian brand since 2007. It is a renown dealer of kids and office furniture locally. Moreover, exporting electric fixtures e.g. switches, LED's, down-lights etc. to Middle East and Africa. We have initiated a number of steps including re-branding, to boost our export in 2020. We have successfully designed our new logo a few months ago through 'Artfolio' and now we are looking for an innovative idea for a letterhead.
Some key points:
• Red, black and white are the three colors used in all our packaging and furniture. (grey is optional)
• Shouldn’t be too wide.
• Use of watermark is preferable.
• You can visit our North American site at www.mapleriseinc.com. Export website of the company will be launched soon. www.mapleriseinc.ca
• Same letterhead will be used locally and internationally.
• Our new logo and sample packaging is attached.

```html
<!DOCTYPE html>
<html lang="en">
<head>
<meta charset="utf-8">
<title>Maplerise Trading Inc. — Letterhead</title>
<link rel="stylesheet" href="https://fonts.googleapis.com/css2?family=Lato:wght@300;400;700&family=Open+Sans:wght@400&family=Pinyon+Script&display=swap">
<style>
  :root {
    --brand-red: #8f0d12;
    --ink: #3a3a3c;
    --ink-strong: #111;
    --paper: #eeedef;
    --backdrop: #f4f4f5;
    --watermark: #dcdbdd;
  }
  * { box-sizing: border-box; margin: 0; padding: 0; }
  html, body { width: 1200px; height: 1012px; overflow: hidden; background: var(--backdrop); }
  .letterhead {
    position: absolute; left: 271px; top: 36px;
    width: 658px; height: 940px;
    background: var(--paper);
    color: var(--ink);
    font-family: "Lato", sans-serif; font-weight: 300;
    overflow: hidden;
  }
  .top-band { position: absolute; left: 0; top: 0; width: 100%; height: 7px; background: var(--brand-red); }
  .brand {
    position: absolute; left: 0; right: 0; top: 48px;
    display: flex; justify-content: center; align-items: center; gap: 10px;
  }
  .brand-mark { width: 34px; height: 34px; border: 2px solid var(--brand-red); border-radius: 4px; }
  .brand-name { font-family: "Lato", sans-serif; font-weight: 400; font-size: 24px; color: var(--ink); letter-spacing: .5px; }
  .watermark {
    position: absolute; left: 355px; top: 658px; width: 303px; height: 282px;
    background: radial-gradient(ellipse at 65% 55%, var(--watermark) 0%, rgba(220,219,221,0.5) 55%, rgba(220,219,221,0) 80%);
  }
  .letter-body { position: absolute; left: 88px; top: 210px; width: 484px; font-size: 10.6px; line-height: 15.6px; }
  .date { margin-bottom: 16px; }
  .recipient strong { font-weight: 700; color: var(--ink-strong); }
  .recipient { margin-bottom: 31px; }
  .salutation { margin-bottom: 16px; }
  .letter-body p.copy { text-align: justify; margin-bottom: 16px; }
  .closing { margin-top: 45px; }
  .signature { font-family: "Pinyon Script", cursive; font-size: 23px; color: var(--ink-strong); margin-top: 6px; padding-left: 4px; }
  .contact {
    position: absolute; top: 862px; font-family: "Open Sans", sans-serif;
    font-size: 11.4px; line-height: 13.6px; color: var(--ink);
  }
  .contact::before { content: ""; display: block; width: 18px; height: 2.5px; background: var(--brand-red); margin-bottom: 16px; }
  .contact-lines { left: 44px; }
  .contact-address { left: 226px; }
  .contact-lines li { list-style: none; display: flex; align-items: center; gap: 5px; }
  .contact-lines svg { width: 8px; height: 8px; fill: var(--brand-red); }
</style>
</head>
<body>
  <main class="letterhead">
    <div class="top-band"></div>
    <header class="brand">
      <span class="brand-mark"></span>
      <span class="brand-name">Maplerise Trading</span>
    </header>

    <div class="watermark" role="img" aria-label="Faint brand watermark in light grey"></div>

    <section class="letter-body">
      <p class="date">01 January 2050</p>
      <p class="recipient"><strong>Company (Pvt) Ltd.</strong><br>PO Box 3355 Mainville St<br>Sample City Country 3355</p>
      <p class="salutation">Dear Laura Pemberton,</p>
      <p class="copy">Lorem ipsum dolor sit amet, consectetuer adipiscing elit, sed diam nonummy nibh euismod tincidunt ut laoreet dolore magna aliquam erat volutpat. Ut wisi enim ad minim veniam, quis nostrud exerci tation ullamcorper suscipit lobortis nisl ut aliquip ex ea commodo consequat. Duis dolore te feugait nulla facilisi. Nam liber tempor cum soluta nobis eleifend option congue nihil imperdiet doming id quod mazim placerat facer possim assum. Lorem ipsum dolor sit amet, consectetuer adipiscing elit, sed diam nonummy nibh euismod tincidunt ut laoreet dolore magna aliquam erat volutpat. Ut wisi enim ad minim veniam, quis nostrud exerci tation ullamcorper suscipit lobortis nisl ut aliquip ex ea commodo consequat.</p>
      <p class="copy">Consectetuer adipiscing elit, sed diam nonummy nibh euismod tincidunt ut laoreet dolore magna aliquam erat volutpat. Ut wisi enim ad minim veniam, quis nostrud exerci tation ullamcorper suscipit lobortis nisl ut aliquip ex ea commodo consequat. Consectetuer adipiscing elit, sed diam nonummy nibh euismod tincidunt ut laoreet dolore magna aliquam erat volutpat. Ut wisi enim ad minim veniam, quis nostrud exerci tation ullamcorper suscipit lobortis nisl ut aliquip ex ea commodo consequat.</p>
      <p class="copy">Consectetuer adipiscing elit, sed diam nonummy nibh euismod tincidunt ut laoreet dolore magna aliquam erat volutpat. Ut wisi enim ad minim veniam, quis nostrud exerci tation ullamcorper suscipit lobortis nisl ut aliquip ex ea commodo consequat. Consectetuer adipiscing elit, sed diam nonummy nibh euismod tincidunt ut laoreet dolore magna aliquam erat volutpat. Ut wisi enim ad minim veniam, quis nostrud exerci tation ullamcorper suscipit lobortis nisl ut aliquip ex ea commodo consequat.</p>
      <p class="closing">Sincerely Yours</p>
      <p class="signature">Daniel Robert Kessler</p>
    </section>

    <ul class="contact contact-lines">
      <li><svg viewBox="0 0 10 10"><path d="M2 0.5 L4 2.8 L3 4 Q4.5 6 6 7 L7.2 6 L9.5 8 L8.2 9.5 Q4 9 0.5 2 Z"/></svg>+1 (888) 555-0142</li>
      <li><svg viewBox="0 0 10 10"><path d="M0 2 H10 V8 H0 Z M0.8 2.6 L5 5.6 L9.2 2.6" fill-rule="evenodd"/></svg>sales@mapleriseinc.com</li>
      <li><svg viewBox="0 0 10 10"><circle cx="5" cy="5" r="4.5"/></svg>www.mapleriseinc.com</li>
    </ul>
    <address class="contact contact-address" style="font-style:normal">
      Maplerise Trading Inc.<br>48 Birchwood Ave #210 Oakridge<br>ON K2R 4P7, Canada
    </address>
  </main>
</body>
</html>
```